Stonefield Crafters Brochure = SCC $$$

this brochure will be used for a canvassing campaign (door to door) appointment setting

the campaign will be for homeowners that would like to do any kind of improvement to their house - home improvement
from EXT paint or roof repair all the way to kitchen and bathroom remodeling

we want to catch the prospect eye with the brochure and to educate our prospect about the different ways they could improve their house step by step to their dream house

Target Market(s)

Homeowners
anyone who would like to improve or fix any part of their house

Industry/Entity Type

Home Improvement

Contact Information for Business Card

the green roof house blueprints on one side
the Stonefield Crafters logo on the other side

Font styles to use
Serif
Decorative

Colors
ffffff
886aae
9bcb3b
e6e6e6

Requirements
Must have
• this is a TRI-FOLD brochure
• call for action -- schedule your free estimate
• or any idea that will lead to set up an appointment with our specialist
• LOOK AT MY WEBSITE TO UNDERSTAND MORE WHAT I LIKE
• WWW.STONEFIELDCRAFTERSCO.EXAMPLE
• services:
• Kitchen Renovations
• Bathroom Renovations
• Modern Landscaping
• Additions + in-law quarters
• Exterior paint +interior paint
• wood replacement + stucco repair
• roof repair
• railling and glass work
Nice to have
• the pictures I have uploaded can use as an example but im open to other ideas...
• THERE IS NO SUBSTITUTE FOR QUALITY.
• the picture of the women in the kitchen--
• i enjoy making food and spending time in my new kitchen, to see my whole family sitting down to eat dinner together in our perfect little kitchen make me so happy
Should not have
• the 2 brochures i have uploaded are for example only

```html
<!DOCTYPE html>
<html lang="en">
<head>
<meta charset="utf-8">
<title>Stonefield Crafters – Tri-fold Brochure</title>
<link href="https://fonts.googleapis.com/css2?family=Montserrat:wght@400;600;700;800&family=Open+Sans:wght@400;600&display=swap" rel="stylesheet">
<style>
:root{
  --green:#8dc63f;
  --green-dark:#6fa82a;
  --charcoal:#2a2a2a;
  --charcoal-2:#363636;
  --ink:#333333;
  --grey:#e6e6e6;
  --mid-grey:#9a9a9a;
  --white:#ffffff;
  --photo-a:#c9c2b6;
  --photo-b:#8e8678;
}
*{box-sizing:border-box;margin:0;padding:0}
html,body{width:880px;height:1200px;overflow:hidden;background:var(--white)}
body{font-family:"Open Sans",Arial,sans-serif;color:var(--ink);position:relative}
.sheet{position:absolute;left:0;width:880px;height:560px;display:grid;grid-template-columns:repeat(3,1fr);overflow:hidden;box-shadow:0 2px 8px rgba(0,0,0,.18)}
.sheet--outside{top:20px;background:var(--white)}
.sheet--inside{top:620px;background:var(--charcoal)}
.panel{position:relative;height:560px;overflow:hidden;border-right:1px solid rgba(0,0,0,.08)}
.photo{position:absolute;left:0;width:100%;background:linear-gradient(160deg,var(--photo-a),var(--photo-b))}
.h{font-family:"Montserrat",Arial,sans-serif;text-transform:uppercase;font-weight:700}
.bar{position:absolute;left:0;right:0;bottom:0;height:40px;background:var(--charcoal);color:var(--white);display:flex;align-items:center;padding:0 16px;font-family:"Montserrat",Arial,sans-serif;font-size:10px;font-weight:700;letter-spacing:.5px;border-top:4px solid var(--green)}
.bar--center{justify-content:center}
.bar--right{justify-content:flex-end}

/* panel 1 outside */
.services-tag{position:absolute;left:16px;top:222px;background:var(--green);color:var(--white);font-size:13px;padding:6px 14px;letter-spacing:1px}
.services-list{position:absolute;left:18px;top:262px;right:14px;list-style:none}
.services-list li{display:flex;align-items:center;gap:8px;font-size:11.5px;line-height:1;padding:5px 0;border-bottom:1px solid var(--grey)}
.services-list li::before{content:"";width:7px;height:7px;background:var(--green);flex:none}
.services-note{position:absolute;left:18px;top:486px;font-size:10px;color:var(--green-dark);letter-spacing:.5px}

/* panel 2 outside */
.logo{display:flex;align-items:center;gap:8px;font-family:"Montserrat",Arial,sans-serif;font-weight:800;text-transform:uppercase;letter-spacing:1px}
.logo-mark{width:16px;height:16px;background:var(--green);flex:none}
.logo--mid{position:absolute;top:48px;left:0;right:0;justify-content:center;color:var(--charcoal);font-size:17px}
.build-band{position:absolute;left:0;top:118px;width:100%;height:200px}
.build-copy{position:absolute;left:22px;right:22px;top:148px;color:var(--white);text-align:center}
.build-copy h2{font-size:30px;letter-spacing:1px}
.build-copy .sub{font-size:11px;font-weight:600;margin:4px 0 10px}
.build-copy p{font-size:10px;line-height:1.5}
.offer-area{position:absolute;left:0;right:0;top:318px;bottom:40px;background:var(--charcoal-2);padding:18px 20px;text-align:center;color:var(--white)}
.offer-area .lead{font-size:10.5px;margin-bottom:10px}
.offer-box{display:flex;align-items:center;justify-content:center;gap:8px;background:var(--white);border-radius:6px;padding:8px 10px;color:var(--charcoal)}
.offer-box .upto{font-family:"Montserrat",sans-serif;font-size:10px;font-weight:700;line-height:1.1;text-align:right}
.offer-box .amount{font-family:"Montserrat",sans-serif;font-size:34px;font-weight:800;color:var(--green)}
.offer-box .tail{font-size:10px;line-height:1.1;text-align:left;font-weight:600}
.offer-area .cta{margin-top:16px;font-size:12px;color:var(--green);line-height:1.4}

/* panel 3 outside */
.cover-top{position:absolute;top:0;left:0;width:100%;height:120px}
.logo--cover{position:absolute;top:34px;right:22px;color:var(--white);font-size:17px}
.quote{position:absolute;left:24px;right:24px;top:340px;font-size:11px;line-height:1.6;color:#555;font-style:italic}
.quote .mark{font-family:"Montserrat",sans-serif;font-size:36px;color:var(--green);line-height:.6;display:block;font-style:normal}
.quote .who{display:block;margin-top:8px;font-style:normal;font-weight:600;color:var(--green-dark);font-size:10px}
.motto{position:absolute;left:24px;right:24px;top:470px;font-size:12px;color:var(--charcoal);text-align:center;letter-spacing:.5px}

/* inside */
.inside-curve{position:absolute;left:0;top:200px;width:880px;height:70px;z-index:2}
.service{position:absolute;left:18px;right:16px;color:#cfcfcf}
.service--a{top:272px}
.service--b{top:392px}
.service-head{display:flex;align-items:center;gap:10px;margin-bottom:8px}
.icon{width:36px;height:36px;border:2px solid var(--green);border-radius:50%;display:flex;align-items:center;justify-content:center;flex:none}
.service-head h3{font-size:12px;color:var(--white);line-height:1.25}
.service p{font-size:9.5px;line-height:1.5}
</style>
</head>
<body>

<!-- OUTSIDE -->
<section class="sheet sheet--outside">
  <article class="panel">
    <div class="photo" style="top:0;height:206px" role="img" aria-label="Photo of a bright renovated white kitchen"></div>
    <div class="services-tag h">Services</div>
    <ul class="services-list">
      <li>Kitchen Renovations</li>
      <li>Bathroom Renovations</li>
      <li>Modern Landscaping</li>
      <li>Additions + in-law quarters</li>
      <li>Exterior paint + interior paint</li>
      <li>Wood replacement + stucco repair</li>
      <li>Roof repair</li>
      <li>Railing and glass work</li>
    </ul>
    <div class="services-note h">We never run out of ideas</div>
    <div class="bar">SCHEDULE YOUR FREE ESTIMATE</div>
  </article>

  <article class="panel">
    <div class="logo logo--mid"><span class="logo-mark"></span>Stonefield Crafters</div>
    <svg class="build-band" viewBox="0 0 293 200" preserveAspectRatio="none">
      <path d="M0 20 Q150 -10 293 10 L293 200 L0 200 Z" fill="var(--green)"/>
    </svg>
    <div class="build-copy">
      <h2 class="h">We Build</h2>
      <div class="sub">Building a better home for you, step by step</div>
      <p>Every project starts with a plan that fits your home, your budget and your family. Our crew handles every step so you can relax and enjoy the result.</p>
    </div>
    <div class="offer-area">
      <div class="lead">Only the FIRST 50 callers this month get up to</div>
      <div class="offer-box">
        <span class="upto">UP<br>TO</span>
        <span class="amount">$5,000</span>
        <span class="tail">off your<br>project</span>
      </div>
      <div class="cta h">Schedule your free consultation<br>for your next project</div>
    </div>
    <div class="bar bar--center">(555) 014-2290</div>
  </article>

  <article class="panel">
    <svg class="cover-top" viewBox="0 0 293 120" preserveAspectRatio="none">
      <rect width="293" height="120" fill="var(--charcoal)"/>
      <path d="M0 96 Q140 70 293 108 L293 120 L0 120 Z" fill="var(--green)"/>
    </svg>
    <div class="logo logo--cover"><span class="logo-mark"></span>Stonefield Crafters</div>
    <div class="photo" style="top:120px;height:206px" role="img" aria-label="Photo of a smiling homeowner in her new kitchen"></div>
    <p class="quote"><span class="mark">“</span>I enjoy making food and spending time in my new kitchen. To see my whole family sitting down to eat dinner together in our perfect little kitchen makes me so happy.<span class="who">— Happy Homeowner</span></p>
    <div class="motto h">There is no substitute for quality</div>
    <div class="bar bar--right">WWW.STONEFIELDCRAFTERSCO.EXAMPLE</div>
  </article>
</section>

<!-- INSIDE -->
<section class="sheet sheet--inside">
  <svg class="inside-curve" viewBox="0 0 880 70" preserveAspectRatio="none">
    <path d="M0 30 Q440 -10 880 30 L880 70 L0 70 Z" fill="var(--charcoal)"/>
    <path d="M0 30 Q440 -10 880 30" fill="none" stroke="var(--green)" stroke-width="6"/>
    <path d="M0 40 Q440 4 880 40" fill="none" stroke="var(--grey)" stroke-width="2"/>
  </svg>

  <article class="panel">
    <div class="photo" style="top:0;height:240px" role="img" aria-label="Photo of a builder on a construction site"></div>
    <div class="service service--a">
      <div class="service-head">
        <span class="icon"><svg width="18" height="18" viewBox="0 0 24 24"><path d="M3 11 L12 3 L21 11 V21 H3 Z" fill="none" stroke="var(--green)" stroke-width="2"/></svg></span>
        <h3 class="h">Design – Build +<br>New Construction</h3>
      </div>
      <p>From first sketch to final walkthrough, we design and build with one team. Clear plans, honest pricing and quality work on every new home we build.</p>
    </div>
    <div class="service service--b">
      <div class="service-head">
        <span class="icon"><svg width="18" height="18" viewBox="0 0 24 24"><path d="M12 3 L5 14 H19 Z M12 21 V14" fill="none" stroke="var(--green)" stroke-width="2"/></svg></span>
        <h3 class="h">Modern<br>Landscapes</h3>
      </div>
      <p>Turn your yard into an outdoor room. Patios, plants, lighting and clean lines that add beauty and value to your home all year long.</p>
    </div>
    <div class="bar">SCHEDULE YOUR FREE ESTIMATE</div>
  </article>

  <article class="panel">
    <div class="photo" style="top:0;height:240px" role="img" aria-label="Photo of a modern renovated kitchen"></div>
    <div class="service service--a">
      <div class="service-head">
        <span class="icon"><svg width="18" height="18" viewBox="0 0 24 24"><rect x="4" y="4" width="16" height="16" fill="none" stroke="var(--green)" stroke-width="2"/><path d="M4 10 H20" stroke="var(--green)" stroke-width="2"/></svg></span>
        <h3 class="h">Kitchen<br>Renovations</h3>
      </div>
      <p>Fresh cabinets, counters and lighting built around how your family cooks and gathers. We plan every detail to make your kitchen the heart of home.</p>
    </div>
    <div class="service service--b">
      <div class="service-head">
        <span class="icon"><svg width="18" height="18" viewBox="0 0 24 24"><path d="M3 21 V10 L10 4 L17 10 V21 Z M17 13 H22 V21 H17" fill="none" stroke="var(--green)" stroke-width="2"/></svg></span>
        <h3 class="h">Additions<br>Remodels</h3>
      </div>
      <p>Need more room? We add bedrooms, in-law quarters and open layouts that blend with your house as if they were always there.</p>
    </div>
    <div class="bar bar--center">(555) 014-2290</div>
  </article>

  <article class="panel">
    <div class="photo" style="top:0;height:240px" role="img" aria-label="Photo of a painter working on a house exterior"></div>
    <div class="service service--a">
      <div class="service-head">
        <span class="icon"><svg width="18" height="18" viewBox="0 0 24 24"><path d="M3 12 H21 V15 Q21 19 17 19 H7 Q3 19 3 15 Z M6 12 V5 H9" fill="none" stroke="var(--green)" stroke-width="2"/></svg></span>
        <h3 class="h">Bathroom<br>Renovations</h3>
      </div>
      <p>Walk-in showers, new tile and smart storage. We build calm, easy to clean bathrooms that feel like a retreat every single day.</p>
    </div>
    <div class="service service--b">
      <div class="service-head">
        <span class="icon"><svg width="18" height="18" viewBox="0 0 24 24"><path d="M2 13 L12 5 L22 13 M5 11 V20 H19 V11" fill="none" stroke="var(--green)" stroke-width="2"/></svg></span>
        <h3 class="h">Roofing +<br>Foundation</h3>
      </div>
      <p>Protect what matters most. We repair roofs, fix leaks and strengthen foundations so your home stays safe, dry and solid for years.</p>
    </div>
    <div class="bar bar--right">WWW.STONEFIELDCRAFTERSCO.EXAMPLE</div>
  </article>
</section>

</body>
</html>
```